Create a channel art for human resources youtube channel

We a are human resource company that want to develop a community on youtube. Our channel is call "TKV Corner" and we will produce videos related to human resources topics like: Strategy, Job Description, selection of workers, workers development, Occupational health, Training, etc.

We need a channel art for our youtube channel that communicate to our viewers what is about the channel.

Attach you can see the logo and icon of the channel, also you can see it here: https://www.vidzora-example.net/channel/QXpLmWt7bRc3dYhFvKaNsEeZ

Target Market(s)

The people who is going to see the art - banner for youtube are persons that work on human resources field

Industry/Entity Type

Business

Font styles to use
Sans Serif

Requirements
Must have
• Must to communicate that our channel is about how to do a better and faster human resources to help business improve there productivity , also workers performances and quality work life. Here are some key words to help you inspire:
• Human Resources
• Performance
• Better
• Faster
• Easier
• Business
• Improve
• Health

```html
<!DOCTYPE html>
<html lang="en">
<head>
<meta charset="utf-8">
<title>TKV Corner – Channel Art</title>
<link rel="stylesheet" href="https://fonts.googleapis.com/css2?family=Lato:wght@300;400;700;900&display=swap">
<style>
  :root {
    --page-bg: #eeeff1;
    --banner-light: #f1f4f8;
    --banner-mid: #dfe5ec;
    --ink: #1f1f21;
    --ink-soft: #2b2d31;
    --white: #ffffff;
    --red: #e2393d;
    --blue: #3aa9e2;
    --yellow: #f2c11c;
    --green: #6db33f;
    --logo-mark: #3a86c8;
    --map-tone: #d6dde6;
    --photo-shirt: #8fb6dc;
    --photo-skin: #a8785a;
    --blur-a: #e9edf2;
    --blur-b: #cfd6de;
  }
  * { box-sizing: border-box; margin: 0; padding: 0; }
  html, body { width: 1200px; height: 675px; overflow: hidden; }
  body {
    background: var(--page-bg);
    font-family: "Lato", Arial, sans-serif;
    color: var(--ink);
    position: relative;
  }
  .banner {
    position: absolute;
    left: 34px;
    width: 1132px;
    overflow: hidden;
  }
  .banner--map {
    top: 82px;
    height: 180px;
    background: linear-gradient(90deg, var(--banner-light), var(--banner-mid));
  }
  .banner--photo {
    top: 365px;
    height: 201px;
    background: linear-gradient(90deg, var(--blur-a) 0%, var(--banner-light) 40%, var(--blur-b) 100%);
  }
  .map-backdrop {
    position: absolute;
    left: 120px; top: 0;
    width: 900px; height: 100%;
    background: radial-gradient(ellipse at 45% 50%, var(--map-tone) 0%, rgba(214,221,230,0) 70%);
    opacity: .8;
  }
  .office-backdrop {
    position: absolute;
    inset: 0;
    background: linear-gradient(90deg, rgba(207,214,222,0) 0%, rgba(207,214,222,.6) 60%, rgba(190,198,208,.7) 100%);
  }
  .brand {
    position: absolute;
    left: 4px;
    top: 12px;
    width: 62px;
    height: 100px;
    background: var(--white);
    display: flex;
    flex-direction: column;
    align-items: center;
    justify-content: center;
    gap: 5px;
  }
  .brand__dot {
    width: 18px; height: 18px;
    border-radius: 50%;
    background: var(--logo-mark);
  }
  .brand__name {
    font-weight: 700;
    font-size: 12px;
    line-height: 1.05;
    text-align: center;
    color: var(--ink-soft);
  }
  .portrait {
    position: absolute;
    left: 112px; top: 12px;
    width: 128px; height: 189px;
    background: linear-gradient(180deg, var(--photo-skin) 0%, var(--photo-skin) 32%, var(--photo-shirt) 34%, #7aa5cf 100%);
    border-radius: 60px 60px 0 0;
    opacity: .9;
  }
  .headline {
    position: absolute;
    text-transform: uppercase;
    line-height: 1;
  }
  .banner--map .headline { left: 168px; top: 30px; }
  .banner--photo .headline { left: 261px; top: 33px; }
  .headline__lead { display: block; font-weight: 400; font-size: 24px; letter-spacing: .5px; }
  .headline__mid { display: block; font-weight: 300; font-size: 52px; letter-spacing: 1px; margin-top: 4px; }
  .headline__key { display: block; font-weight: 900; font-size: 66px; letter-spacing: 1px; margin-top: 0; }
  .features {
    position: absolute;
    display: flex;
    list-style: none;
  }
  .banner--map .features { left: 612px; top: 50px; gap: 27px; }
  .banner--photo .features { left: 666px; top: 53px; gap: 22px; }
  .feature {
    width: 103px; height: 103px;
    display: flex;
    flex-direction: column;
    align-items: center;
    justify-content: flex-end;
    padding-bottom: 12px;
    color: var(--white);
    font-weight: 700;
    font-size: 15px;
    line-height: 1.05;
    text-align: center;
    text-transform: uppercase;
    box-shadow: 0 2px 4px rgba(0,0,0,.15);
  }
  .banner--photo .feature { width: 94px; height: 94px; padding-bottom: 10px; font-size: 14px; }
  .feature svg { width: 34px; height: 34px; margin-bottom: 8px; }
  .banner--photo .feature svg { width: 30px; height: 30px; margin-bottom: 7px; }
  .feature--red { background: var(--red); }
  .feature--blue { background: var(--blue); }
  .feature--yellow { background: var(--yellow); }
  .feature--green { background: var(--green); }
</style>
</head>
<body>

<section class="banner banner--map">
  <div class="map-backdrop" role="img" aria-label="Faint world map in the background"></div>
  <div class="brand"><span class="brand__dot"></span><span class="brand__name">TKV<br>Corner</span></div>
  <h1 class="headline">
    <span class="headline__lead">Simple solutions</span>
    <span class="headline__mid">For peoples</span>
    <span class="headline__key">Proplems!</span>
  </h1>
  <ul class="features">
    <li class="feature feature--red">
      <svg viewBox="0 0 24 24" fill="#fff"><path d="M2 10h4v11H2zM8 21V10l5-8c1.5 0 2.5 1 2 3l-1 4h6c1.2 0 2 1 1.8 2.2l-1.6 7.6c-.2 1.2-1.1 2.2-2.3 2.2z"/></svg>
      Better<br>services
    </li>
    <li class="feature feature--blue">
      <svg viewBox="0 0 24 24" fill="none" stroke="#fff" stroke-width="2"><path d="M5 22V3"/><path d="M5 4c5-3 9 3 14 0v10c-5 3-9-3-14 0" fill="#fff"/></svg>
      Fast<br>services
    </li>
    <li class="feature feature--yellow">
      <svg viewBox="0 0 24 24" fill="#fff"><path d="M5 2l14 11h-7l4 8-3 1.5-4-8-4 5z"/></svg>
      Easy to<br>use
    </li>
    <li class="feature feature--green">
      <svg viewBox="0 0 24 24" fill="#fff"><path d="M2 20h3v-4H2zM7 20h3v-7H7zM12 20h3v-9h-3zM17 20h3V8h-3z"/><path d="M3 12l6-5 4 3 7-6" fill="none" stroke="#fff" stroke-width="2"/><path d="M17 2h5v5z"/></svg>
      Improve<br>business
    </li>
  </ul>
</section>

<section class="banner banner--photo">
  <div class="office-backdrop" role="img" aria-label="Softly blurred office interior in the background"></div>
  <div class="brand"><span class="brand__dot"></span><span class="brand__name">TKV<br>Corner</span></div>
  <div class="portrait" role="img" aria-label="Photo of a smiling businessman in a blue shirt with arms crossed"></div>
  <h1 class="headline">
    <span class="headline__lead">Simple solutions</span>
    <span class="headline__mid">For peoples</span>
    <span class="headline__key">Proplems!</span>
  </h1>
  <ul class="features">
    <li class="feature feature--red">
      <svg viewBox="0 0 24 24" fill="#fff"><path d="M2 10h4v11H2zM8 21V10l5-8c1.5 0 2.5 1 2 3l-1 4h6c1.2 0 2 1 1.8 2.2l-1.6 7.6c-.2 1.2-1.1 2.2-2.3 2.2z"/></svg>
      Better<br>services
    </li>
    <li class="feature feature--blue">
      <svg viewBox="0 0 24 24" fill="none" stroke="#fff" stroke-width="2"><path d="M5 22V3"/><path d="M5 4c5-3 9 3 14 0v10c-5 3-9-3-14 0" fill="#fff"/></svg>
      Fast<br>services
    </li>
    <li class="feature feature--yellow">
      <svg viewBox="0 0 24 24" fill="#fff"><path d="M5 2l14 11h-7l4 8-3 1.5-4-8-4 5z"/></svg>
      Easy to<br>use
    </li>
    <li class="feature feature--green">
      <svg viewBox="0 0 24 24" fill="#fff"><path d="M2 20h3v-4H2zM7 20h3v-7H7zM12 20h3v-9h-3zM17 20h3V8h-3z"/><path d="M3 12l6-5 4 3 7-6" fill="none" stroke="#fff" stroke-width="2"/><path d="M17 2h5v5z"/></svg>
      Improve<br>business
    </li>
  </ul>
</section>

</body>
</html>
```